Dorsey K. Wendell Business Card

We need a business card for our company Dorsey K. Wendell Heating & Plumbing to be distributed to potential customers. It should follow the color scheme of our logo and have a modern upscale and masculine look.

The logo is attached and the info below should also be included:

5187 W. Cedar Brook Rd.
Hollisburg, PA 17630

Russell T. Wendell
(717) 592-0817
russelltwendell@fernmail.net
dorseykwendell.net
PA #093148

Industry/Entity Type

Business

Contact Information for Business Card

5187 W. Cedar Brook Rd.
Hollisburg, PA 17630

Russell T. Wendell
(717) 592-0817
russelltwendell@fernmail.net
dorseykwendell.net
PA #093148

Colors

Designer to choose colors to be used in the design.

Requirements
Must have
• Information above included

```html
<!DOCTYPE html>
<html lang="en">
<head>
<meta charset="utf-8">
<title>Dorsey K. Wendell Business Card</title>
<link rel="stylesheet" href="https://fonts.googleapis.com/css2?family=Open+Sans:wght@400;700;800&display=swap">
<style>
  :root {
    --brand-blue: #0a52a5;
    --brand-green: #a6d33a;
    --charcoal: #2b2b2b;
    --paper: #ffffff;
    --backdrop: #ecebe8;
    --muted-blue: #b9cbe6;
  }
  * { box-sizing: border-box; margin: 0; padding: 0; }
  html, body {
    width: 1200px; height: 894px; overflow: hidden;
    background: var(--backdrop);
    font-family: "Open Sans", sans-serif;
  }
  .stage { position: relative; width: 1200px; height: 894px; }

  .card {
    position: absolute;
    width: 540px; height: 309px;
    background: var(--paper);
    overflow: hidden;
    box-shadow: 0 6px 18px rgba(0,0,0,0.18);
  }
  .card-front { left: 80px; top: 118px; }
  .card-back  { left: 580px; top: 466px; }

  /* front bands */
  .band-top { position: absolute; left: 0; right: 0; top: 0; height: 9px; background: var(--brand-blue); }
  .rule-top { position: absolute; left: 0; right: 0; top: 15px; height: 3px; background: var(--brand-green); }
  .rule-bottom { position: absolute; left: 0; right: 0; bottom: 15px; height: 3px; background: var(--brand-green); }
  .band-bottom { position: absolute; left: 0; right: 0; bottom: 0; height: 9px; background: var(--brand-blue); }

  /* wordmark */
  .wordmark-area {
    position: absolute; left: 0; right: 0;
    display: flex; align-items: center; justify-content: center;
  }
  .card-front .wordmark-area { top: 18px; bottom: 18px; }
  .card-back .wordmark-area { top: 0; height: 150px; }
  .wordmark {
    display: flex; align-items: center; gap: 14px;
    color: var(--brand-blue);
    font-weight: 800;
    text-transform: uppercase;
    line-height: 1;
    white-space: nowrap;
  }
  .wordmark-square { width: 52px; height: 52px; background: var(--brand-blue); flex: none; }
  .wordmark-name { display: block; font-size: 31px; letter-spacing: 0.5px; }
  .wordmark-trade { display: block; font-size: 13px; letter-spacing: 2.4px; margin-top: 7px; }
  .wordmark-compact .wordmark-square { width: 44px; height: 44px; }
  .wordmark-compact .wordmark-name { font-size: 26px; }
  .wordmark-compact .wordmark-trade { font-size: 11px; letter-spacing: 2px; margin-top: 6px; }

  /* back panels */
  .back-rule { position: absolute; left: 0; right: 0; top: 150px; height: 3px; background: var(--brand-green); }
  .back-base { position: absolute; left: 0; right: 0; top: 153px; bottom: 0; background: var(--charcoal); }
  .holder-panel {
    position: absolute; left: 0; top: 153px; width: 272px; bottom: 22px;
    background: var(--brand-blue);
    border-right: 3px solid var(--brand-green);
    display: flex; flex-direction: column; justify-content: center;
    padding-left: 24px;
  }
  .holder-name { color: var(--paper); font-weight: 700; font-size: 22px; white-space: nowrap; }
  .holder-license { color: var(--muted-blue); font-size: 13px; margin-top: 10px; margin-left: 92px; }
  .base-rule { position: absolute; left: 0; right: 0; bottom: 10px; height: 3px; background: var(--brand-green); }

  .contact-list {
    position: absolute; left: 294px; top: 170px; list-style: none;
    color: var(--paper); font-size: 12.5px; line-height: 1.25;
    white-space: nowrap;
  }
  .contact-list li { display: flex; align-items: flex-start; gap: 12px; margin-bottom: 6px; }
  .contact-icon { width: 14px; height: 14px; flex: none; margin-top: 1px; }
  .contact-icon * { fill: none; stroke: var(--brand-green); stroke-width: 1.6; }
  .contact-icon .solid { fill: var(--brand-green); stroke: none; }
</style>
</head>
<body>
<main class="stage">

  <section class="card card-front" aria-label="Card front">
    <div class="band-top"></div>
    <div class="rule-top"></div>
    <div class="wordmark-area">
      <div class="wordmark">
        <span class="wordmark-square"></span>
        <span>
          <span class="wordmark-name">Dorsey K. Wendell</span>
          <span class="wordmark-trade">Heating &amp; Plumbing</span>
        </span>
      </div>
    </div>
    <div class="rule-bottom"></div>
    <div class="band-bottom"></div>
  </section>

  <section class="card card-back" aria-label="Card back">
    <div class="wordmark-area">
      <div class="wordmark wordmark-compact">
        <span class="wordmark-square"></span>
        <span>
          <span class="wordmark-name">Dorsey K. Wendell</span>
          <span class="wordmark-trade">Heating &amp; Plumbing</span>
        </span>
      </div>
    </div>
    <div class="back-rule"></div>
    <div class="back-base"></div>
    <div class="holder-panel">
      <p class="holder-name">Russell T. Wendell</p>
      <p class="holder-license">PA #093148</p>
    </div>
    <div class="base-rule"></div>

    <ul class="contact-list">
      <li>
        <svg class="contact-icon" viewBox="0 0 16 16" aria-hidden="true"><path class="solid" d="M3 1.5l3 .5 1 3.2-1.8 1.3a9 9 0 0 0 4.3 4.3L10.8 9l3.2 1 .5 3-2 1.5C7 14.5 1.5 9 1.5 3.5z"/></svg>
        <span>(717) 592-0817</span>
      </li>
      <li>
        <svg class="contact-icon" viewBox="0 0 16 16" aria-hidden="true"><circle cx="8" cy="8" r="2.6"/><path d="M10.6 5.5v3.6c0 1.6 2.9 1.6 2.9-1.1A5.5 5.5 0 1 0 11 12.6"/></svg>
        <span>russelltwendell@fernmail.net</span>
      </li>
      <li>
        <svg class="contact-icon" viewBox="0 0 16 16" aria-hidden="true"><circle cx="8" cy="8" r="6.2"/><path d="M1.8 8h12.4M8 1.8c-3 3.4-3 9 0 12.4M8 1.8c3 3.4 3 9 0 12.4"/></svg>
        <span>www.dorseykwendell.net</span>
      </li>
      <li>
        <svg class="contact-icon" viewBox="0 0 16 16" aria-hidden="true"><path class="solid" d="M8 1a5 5 0 0 0-5 5c0 3.6 5 9 5 9s5-5.4 5-9a5 5 0 0 0-5-5zm0 7a2 2 0 1 1 0-4 2 2 0 0 1 0 4z"/></svg>
        <span>5187 W. Cedar Brook Rd.<br>Hollisburg, PA 17630</span>
      </li>
    </ul>
  </section>

</main>
</body>
</html>
```